We Import and supply LED Lighting products (High Bays, Flood Lights, Bulbs, Down Lights, Strip Lighting, Night Lights.) and we are after a brochure design that communicates these product points below..

1. Environmentally Friendly.
2. Recyclable
3. Energy Saving
3. Cost Savings for the customer (big and small business)
4. Long Life Span.
5. Lower Maintenance Costs.
6. Importing
7. QUALITY PRODUCTS

The brochure needs to reflect that LED lighting is a safer 'lighting' solution for the environment and also to reflect big cost savings to big and small business ... I have highlighted some colours below but will leave this to the designer to decide on.

I have included some photos that resemble the type of other LED Lighting we sell.

Kind Regards

File 3 & File 5 can't be opened so please ignore.

Target Market(s)

Industrial / Warehousing... (Highbays & Flood Lights)
Domestic: ..... Bulbs & Strip Lighting

Industry/Entity Type

Small Business

Requirements
Must have
• Your professional experience in graphic design... show me that you can produce a professional look, not just a rush job with bad spelling.

Definitely depicts that we sell Quality LED Lighting with very competitive pricing.

Wholesale and Retail.

Our Logo.. this is the image I have uploaded, '"purple circle with grey wings"
Nice to have
• images and or symbols that depict recyclable, environmentally safe. energy saving and maybe a stack of coins that show money that can be saved (especially on the highbays)
Should not have
• copying the brochure I have uploaded and just adding colour!...

```html
<!DOCTYPE html>
<html lang="en">
<head>
<meta charset="utf-8">
<title>Lumora Imports – LED Lighting Brochure</title>
<link href="https://fonts.googleapis.com/css2?family=Questrial&display=swap" rel="stylesheet">
<style>
  :root{
    --magenta:#c8267f;
    --purple:#7b2b8c;
    --pink-deep:#b2227a;
    --ink:#5d5d66;
    --ink-soft:#8a8a92;
    --paper:#ffffff;
    --tint:#eef0e2;
    --stage:#e6e6e8;
    --photo-a:#f3f3f5;
    --photo-b:#a9abb2;
    --badge:#6fae3a;
  }
  *{box-sizing:border-box;margin:0;padding:0}
  html,body{width:1200px;height:677px;overflow:hidden}
  body{background:var(--stage);font-family:"Questrial",sans-serif;color:var(--ink);position:relative}

  .spread{position:absolute;top:115px;width:576px;height:446px;background:var(--paper);box-shadow:0 2px 10px rgba(0,0,0,.12);overflow:hidden}
  .spread--outer{left:16px}
  .spread--inner{left:608px}
  .spread__art{position:absolute;inset:0;width:576px;height:446px}
  .fold{position:absolute;top:0;bottom:0;width:1px;background:rgba(0,0,0,.05)}

  .abs{position:absolute}
  .photo{position:absolute;border-radius:50%;border:3px solid var(--purple);background:radial-gradient(circle at 40% 40%,var(--photo-a),var(--photo-b));}
  .photo--strip{background:radial-gradient(circle at 45% 45%,#d9f0ff,#8c6fc0 55%,#5a4d7e)}
  .photo--night{background:radial-gradient(circle at 45% 45%,#f6dbe7,#c98aa8)}

  .badges{display:flex;gap:10px}
  .badge{width:20px;height:20px;background:var(--badge)}
  .badge--round{border-radius:50%}
  .badge--soft{border-radius:5px;background:#8fbf55}

  .help-title{color:var(--magenta);font-size:11px;line-height:1.15;letter-spacing:.3px;font-weight:400}
  .help-copy{font-size:6px;line-height:1.5;text-align:right;color:var(--ink-soft)}

  .benefits{color:#fff}
  .benefits h2{font-size:10.5px;font-weight:400;margin-bottom:4px}
  .benefits h3{font-size:10px;font-weight:400;margin:9px 0 3px;padding-bottom:2px;border-bottom:1px solid rgba(255,255,255,.35)}
  .benefits p{font-size:5.6px;line-height:1.5;padding-left:8px}

  .contact h4{color:var(--magenta);font-size:6.5px;font-weight:400;letter-spacing:.4px;line-height:1.35}
  .contact p{font-size:5.6px;line-height:1.5;color:var(--ink-soft);margin-top:4px}
  .web{font-size:7px;letter-spacing:2px;color:var(--ink-soft)}

  .brand{display:flex;align-items:center;gap:5px;color:var(--purple);font-size:15px;letter-spacing:.3px}
  .brand__dot{width:12px;height:12px;border-radius:50%;background:var(--purple)}
  .tagline{font-size:6px;letter-spacing:2.5px;color:var(--ink-soft)}
  .offer{text-align:right;color:var(--magenta);font-size:10px;line-height:1.15}
  .offer ul{list-style:none;color:var(--ink-soft);font-size:7.5px;line-height:1.3;margin-top:3px;letter-spacing:.3px}

  .band-title{font-size:10px;color:#fff}
  .band-title--grey{color:var(--ink)}
  .product{font-size:11px;color:var(--magenta);line-height:1.1}
  .product--light{color:#fff}
  .product small{display:block;font-size:7px;letter-spacing:.4px}
  .spec{font-size:5px;line-height:1.5;color:var(--ink-soft);display:grid;grid-template-columns:auto auto;column-gap:8px}
  .spec span:nth-child(even){text-align:right}
  .spec--light{color:#fff}
  .note{font-size:5.5px;line-height:1.5;color:var(--ink-soft)}
  .note--light{color:#fff}
</style>
</head>
<body>

<section class="spread spread--outer" aria-label="Brochure outer side">
  <svg class="spread__art" viewBox="0 0 576 446" aria-hidden="true">
    <defs>
      <linearGradient id="tintOuter" x1="0" y1="0" x2="0" y2="1">
        <stop offset="0" stop-color="#ffffff"/><stop offset="1" stop-color="#eef0e2"/>
      </linearGradient>
      <linearGradient id="magentaOuter" x1="0" y1="0" x2="0" y2="1">
        <stop offset="0" stop-color="#d22e86"/><stop offset="1" stop-color="#8d2c8d"/>
      </linearGradient>
    </defs>
    <rect x="0" y="300" width="576" height="146" fill="url(#tintOuter)"/>
    <path d="M192 0 H384 V276 Q300 300 192 338 Z" fill="url(#magentaOuter)"/>
    <path d="M0 364 Q100 330 192 338" fill="none" stroke="#7b2b8c" stroke-width="2"/>
    <path d="M0 250 Q70 232 96 214" fill="none" stroke="#7b2b8c" stroke-width="2"/>
    <path d="M384 430 Q500 400 576 300 Q510 392 384 436 Z" fill="#7b2b8c"/>
  </svg>
  <div class="fold" style="left:192px"></div>
  <div class="fold" style="left:384px"></div>

  <div class="badges abs" style="left:16px;top:18px">
    <div class="badge badge--round"></div>
    <div class="badge badge--soft"></div>
    <div class="badge badge--round" style="background:#4f9a3b"></div>
    <div class="badge badge--round" style="background:#9ccc5a"></div>
  </div>
  <div class="photo" style="left:34px;top:88px;width:124px;height:124px" role="img" aria-label="LED flood light photo"></div>
  <div class="photo photo--strip" style="left:118px;top:72px;width:46px;height:46px" role="img" aria-label="Reel of RGB LED strip lighting"></div>
  <h2 class="help-title abs" style="left:16px;top:258px">WE ARE HERE<br>TO HELP</h2>
  <p class="help-copy abs" style="left:56px;top:276px;width:124px">You may have in mind LED products not mentioned within this brochure, simply send an email with your enquiry with as much detail as possible and we would be happy to source and quote for you.</p>

  <div class="benefits abs" style="left:202px;top:14px;width:172px">
    <h2>A few benefits of LED Lighting</h2>
    <p>LED lights are the most energy efficient lighting available today and most cost effective, they are made from non-toxic materials, generate virtually no heat and are fully recyclable.</p>
    <h3>Environmentally Friendly</h3>
    <p>LED lights are an eco-friendly form of lighting as they do not contain mercury or other harmful gases or any harmful UV rays.</p>
    <h3>Long Life Span</h3>
    <p>LED lights have a super long life span of 50000+ hours meaning big savings on your maintenance costs (no more blown lamps or replacement).</p>
    <h3>Safety</h3>
    <p>Most LED lights operate at low voltage so are cool to touch and much safer to handle during installation and maintenance.</p>
    <h3>Insects</h3>
    <p>Insect attraction is greatly reduced due to minimal UV light and heat.</p>
  </div>
  <div class="contact abs" style="left:206px;top:346px;width:170px">
    <h4>FOR ALL PRICING AND<br>QUOTING PLEASE CONTACT:</h4>
    <p>Nadia Reyes<br>Mobile: 0400 555 019<br>Email: hello@lumoraimports.example</p>
  </div>
  <p class="web abs" style="left:206px;top:412px">www.lumoraimports.example</p>

  <div class="brand abs" style="right:14px;top:22px"><span class="brand__dot"></span>Lumora Imports</div>
  <p class="tagline abs" style="right:14px;top:46px">Importer &amp; Supplier</p>
  <div class="offer abs" style="right:16px;top:104px">
    QUALITY LED<br>PRODUCTS
    <ul><li>WHOLESALE</li><li>RETAIL</li><li>COMMERCIAL</li><li>DOMESTIC</li></ul>
  </div>
</section>

<section class="spread spread--inner" aria-label="Brochure inner side">
  <svg class="spread__art" viewBox="0 0 576 446" aria-hidden="true">
    <defs>
      <linearGradient id="tintInner" x1="0" y1="0" x2="0" y2="1">
        <stop offset="0" stop-color="#ffffff"/><stop offset="1" stop-color="#eef0e2"/>
      </linearGradient>
      <linearGradient id="magentaInner" x1="0" y1="0" x2="1" y2="1">
        <stop offset="0" stop-color="#d22e86"/><stop offset="1" stop-color="#8d2c8d"/>
      </linearGradient>
    </defs>
    <rect x="0" y="320" width="576" height="126" fill="url(#tintInner)"/>
    <path d="M0 0 H192 V150 Q110 178 0 172 Z" fill="url(#magentaInner)"/>
    <path d="M0 302 Q110 282 192 264 V446 H0 Z" fill="url(#magentaInner)"/>
    <path d="M384 0 H576 V236 Q470 256 432 214 Q404 150 392 90 Q388 40 384 30 Z" fill="url(#magentaInner)"/>
    <path d="M192 294 Q290 268 384 282" fill="none" stroke="#7b2b8c" stroke-width="1.5"/>
  </svg>
  <div class="fold" style="left:192px"></div>
  <div class="fold" style="left:384px"></div>

  <p class="band-title abs" style="left:14px;top:8px">Environmentally Friendly</p>
  <p class="product product--light abs" style="left:14px;top:28px">LED Highbays</p>
  <div class="spec spec--light abs" style="left:14px;top:52px;width:104px">
    <span>Input Voltage</span><span>100-240V</span>
    <span>Light Source</span><span>Brightcore COB</span>
    <span>Consumption</span><span>100-200W</span>
    <span>Efficiency</span><span>90-100 lm/W</span>
    <span>Beam Angles</span><span>60° / 90° / 120°</span>
    <span>Colour Temp</span><span>3000K-6500K</span>
    <span>Driver</span><span>Steadyvolt</span>
    <span>Power Factor</span><span>&gt;0.95</span>
    <span>Working Life</span><span>&gt;50000hrs</span>
  </div>
  <div class="photo" style="left:124px;top:60px;width:64px;height:64px" role="img" aria-label="LED highbay light photo"></div>
  <p class="product abs" style="left:14px;top:190px">LED Bulbs</p>
  <div class="spec abs" style="left:14px;top:208px;width:168px">
    <span>Power Consumption</span><span>3W / 5W / 7W / 9W</span>
    <span>Base Type</span><span>B22 / E27</span>
    <span>Input Voltage</span><span>AC110-240V</span>
    <span>Colour</span><span>Cool White / Warm White</span>
    <span>Colour Temp</span><span>2800-6500K</span>
  </div>
  <div class="photo" style="left:6px;top:312px;width:108px;height:108px" role="img" aria-label="LED bulb photo"></div>

  <p class="band-title band-title--grey abs" style="left:220px;top:8px">Big Reduction in Power Costs</p>
  <p class="product abs" style="left:262px;top:26px">LED Flood Lights</p>
  <div class="spec abs" style="left:204px;top:46px;width:170px">
    <span>Power Consumption</span><span>10W / 20W / 30W / 50W</span>
    <span>Light Source</span><span>Brightcore COB</span>
    <span>Luminous Efficiency</span><span>90-100 lm/W</span>
    <span>Beam Angle</span><span>120°</span>
    <span>Colour</span><span>CW / WW / R / G / B / RGB</span>
    <span>IP Grade</span><span>IP65</span>
    <span>Working Life</span><span>&gt;50000hrs</span>
  </div>
  <div class="photo" style="left:246px;top:108px;width:72px;height:72px" role="img" aria-label="LED flood light photo"></div>
  <p class="product abs" style="left:204px;top:188px">LED STRIP LIGHTING<small>HEAVY DUTY / WATERPROOF</small></p>
  <p class="note abs" style="left:204px;top:216px;width:120px">Input Voltage AC110 / 240V<br>Size 5m / Roll<br>Grade IP65<br>Colour CW WW R G B RGB<br>(Pre-made to your length requirements, up to 50m)</p>
  <div class="photo photo--strip" style="left:284px;top:300px;width:92px;height:92px" role="img" aria-label="Reel of RGB LED strip lighting"></div>

  <p class="band-title abs" style="left:400px;top:8px">2 Year Warranty (all products)</p>
  <p class="product product--light abs" style="left:404px;top:24px">LED COB Downlights</p>
  <div class="spec spec--light abs" style="left:404px;top:46px;width:84px">
    <span>Power</span><span>3W / 5W / 7W</span>
    <span>Light Source</span><span>COB</span>
    <span>Input</span><span>AC240V</span>
    <span>Beam</span><span>60°</span>
    <span>Colour</span><span>CW / WW</span>
    <span>Cut Out</span><span>70mm</span>
    <span>Dimmable</span><span>Non-dim</span>
  </div>
  <div class="photo" style="left:500px;top:32px;width:64px;height:64px" role="img" aria-label="LED COB downlight photo"></div>
  <p class="product product--light abs" style="left:490px;top:108px">LED Deck Lights</p>
  <p class="note note--light abs" style="left:470px;top:126px;width:98px;text-align:right">Power Consumption 3W<br>Cut Hole 30mm<br>Great for Pathway Lights<br>Colour CW WW R G B RGB<br>Pre-made to your design</p>
  <p class="note note--light abs" style="left:470px;top:176px;width:98px;text-align:right">100W Power Converter 240V<br>Run up to 30 deck lights<br>from one power point</p>
  <div class="photo" style="left:394px;top:146px;width:50px;height:50px" role="img" aria-label="LED deck light photo"></div>
  <div class="photo" style="left:418px;top:198px;width:42px;height:42px" role="img" aria-label="LED power converter photo"></div>
  <p class="product abs" style="left:404px;top:268px">LED NIGHT<br>LIGHTS</p>
  <p class="note abs" style="left:404px;top:298px;width:70px">Audio Turtle<br>Plays 'your' music<br>3x Batteries / 240V</p>
  <div class="photo photo--night" style="left:478px;top:262px;width:86px;height:86px" role="img" aria-label="Turtle night light photo"></div>
</section>

</body>
</html>
```